Flyer Design for Upcoming Baseball Clinics, Camps, and Academies

What We Need:
We are looking for a design template we can use for our upcoming sports camps, clinics, and academies. We do elite level training with youth to professional athletes and brand awareness is our number one concern right now.

Ideally this template can be used across multiple sports. Here is our premise:

Clinics (1-Day Event to attract 50+ Athletes)
Camps (2-4 Day Events looking to attract 100+)
Academies (More intimate and skill specific. lasts 6-8 weeks. 10-20 athletes)

Our plan is to do this for Baseball, Football, Basketball, and Lacrosse.

The ideal situation is to be able to use this as a template so we can just edit the document in the future.

Target Market(s)

Prep: Middle School Athletes / ELITE: High School Athletes

Industry/Entity Type

Training

Requirements
Must have
• Things to include:
• Logo, Dates, Times, Investment, Description, Benefits, our mission statement, etc. Our specific colors, specific font family (Bunken Tech Sans Wide), follow our branding deck which is attached.
• Info:
• K7Z BASEBALL CLINIC
• Date: November 11th, 2017
• AGES: PREP: (5th to 8th Grade). ELITE (9th-12th Grade)
• Registration: 8:00am - 9:00 am / 11:00 am - Noon
• Times:
• PREP: 9:00am - 11:00 am
• ELITE: Noon - 2pm
• Investment: $199
• Current Members: $99
Nice to have
• It would be nice to see our mission statement tied in somehow in a unique way. Also maybe a testimonial or two from our pro athletes??
Should not have
• Fake Images: Any Image used needs to be real and give off an authentic feel of a baseball player and the culture.

```html
<!DOCTYPE html>
<html lang="en">
<head>
<meta charset="UTF-8">
<title>K7Z Baseball Clinic Flyer</title>
<link href="https://fonts.googleapis.com/css2?family=Michroma&family=Orbitron:wght@600;800&display=swap" rel="stylesheet">
<style>
  :root {
    --teal: #1b8f9f;
    --slate: #3e474a;
    --white: #ffffff;
    --ink: #2b2f31;
    --backdrop: #e9eaeb;
  }
  * { box-sizing: border-box; margin: 0; padding: 0; }
  html, body {
    width: 1200px; height: 966px; overflow: hidden;
    background: var(--backdrop);
  }
  .canvas {
    width: 1200px; height: 966px;
    display: flex; align-items: center; justify-content: center;
  }
  .flyer {
    position: relative;
    width: 720px; height: 932px;
    background: var(--white);
    font-family: "Michroma", sans-serif;
    color: var(--ink);
    overflow: hidden;
    box-shadow: 0 4px 18px rgba(0,0,0,.18);
  }
  .photo-grid { position: absolute; left: 0; top: 0; width: 720px; height: 400px; }
  .brand {
    position: absolute; left: 28px; top: 66px;
    display: flex; align-items: center; gap: 10px;
    font-family: "Michroma", sans-serif;
    font-size: 26px; color: var(--white); letter-spacing: 2px;
  }
  .brand-mark { width: 14px; height: 14px; background: var(--white); }

  .mission { position: absolute; left: 0; top: 400px; width: 720px; height: 100px; }
  .mission svg { position: absolute; inset: 0; width: 100%; height: 100%; }
  .mission-text {
    position: absolute; left: 70px; right: 80px; top: 8px;
    text-align: center; color: var(--white);
  }
  .mission-label { font-family: "Orbitron", sans-serif; font-weight: 800; font-size: 14px; letter-spacing: 1px; }
  .mission-line { font-size: 13px; margin-top: 4px; letter-spacing: .5px; }
  .mission-headline { font-family: "Orbitron", sans-serif; font-weight: 800; font-size: 30px; letter-spacing: 2px; margin-top: 2px; }

  .offerings { position: absolute; left: 0; top: 500px; width: 720px; height: 240px; }
  .tagline {
    text-align: center; font-family: "Orbitron", sans-serif; font-weight: 600;
    font-size: 15.5px; line-height: 1.45; padding-top: 10px; letter-spacing: .4px;
  }
  .programs { display: flex; justify-content: space-around; padding: 10px 30px 0; }
  .program { width: 210px; text-align: center; }
  .program-badge {
    width: 112px; height: 112px; border-radius: 50%;
    background: var(--teal); color: var(--white);
    display: flex; align-items: center; justify-content: center;
    margin: 0 auto; font-size: 11px; letter-spacing: 0;
  }
  .program-note { font-size: 10.5px; line-height: 1.45; margin-top: 9px; }

  .event-band {
    position: absolute; left: 0; top: 740px; width: 720px; height: 62px;
    background: var(--teal); color: var(--white); text-align: center; padding-top: 10px;
  }
  .event-title { font-family: "Orbitron", sans-serif; font-weight: 800; font-size: 19px; letter-spacing: 1.5px; }
  .event-date { font-size: 13px; margin-top: 4px; }

  .details {
    position: absolute; left: 0; top: 802px; width: 720px; height: 130px;
    background: var(--slate); color: var(--white);
    display: grid; grid-template-columns: 400px 320px;
    font-size: 12px; line-height: 1.55;
  }
  .details-col { padding: 14px 0 0 44px; white-space: nowrap; }
  .details-col + .details-col { border-left: 3px solid var(--teal); padding-left: 30px; margin: 8px 0 12px; padding-top: 6px; }
  .details-block + .details-block { margin-top: 8px; }
</style>
</head>
<body>
<div class="canvas">
  <article class="flyer">
    <svg class="photo-grid" viewBox="0 0 720 400" xmlns="http://www.w3.org/2000/svg">
      <defs>
        <linearGradient id="fieldDugout" x1="0" y1="0" x2="0" y2="1">
          <stop offset="0" stop-color="#6f7a73"/><stop offset=".45" stop-color="#b74a3e"/><stop offset="1" stop-color="#4f8a3c"/>
        </linearGradient>
        <linearGradient id="fieldTalk" x1="0" y1="0" x2="0" y2="1">
          <stop offset="0" stop-color="#7fa85a"/><stop offset=".5" stop-color="#a8403a"/><stop offset="1" stop-color="#4e8a34"/>
        </linearGradient>
        <linearGradient id="fieldSwing" x1="0" y1="0" x2="0" y2="1">
          <stop offset="0" stop-color="#3f7d36"/><stop offset=".4" stop-color="#c54a36"/><stop offset="1" stop-color="#b6916b"/>
        </linearGradient>
      </defs>
      <rect width="720" height="400" fill="#ffffff"/>
      <polygon points="0,0 392,0 381,180 0,195" fill="url(#fieldDugout)" role="img" aria-label="Photo: coach huddling with young players in dugout by the field"/>
      <polygon points="0,206 380,191 368,400 0,400" fill="url(#fieldTalk)" role="img" aria-label="Photo: coach giving one-on-one advice to a young batter"/>
      <polygon points="404,0 720,0 720,400 380,400" fill="url(#fieldSwing)" role="img" aria-label="Photo: batter in red jersey number 23 mid-swing at the plate"/>
    </svg>
    <div class="brand"><span class="brand-mark"></span>K7Z</div>

    <section class="mission">
      <svg viewBox="0 0 720 100" preserveAspectRatio="none">
        <rect width="720" height="100" fill="#3e474a"/>
        <polygon points="78,0 640,0 632,100 60,100" fill="#1b8f9f"/>
        <rect x="650" y="0" width="4" height="100" fill="#ffffff"/>
        <rect x="50" y="0" width="4" height="100" fill="#ffffff"/>
      </svg>
      <div class="mission-text">
        <div class="mission-label">OUR MISSION</div>
        <div class="mission-line">TO TRAIN, INSTRUCT, MOTIVATE &amp; EMPOWER</div>
        <div class="mission-headline">THE ATHLETE INSIDE YOU</div>
      </div>
    </section>

    <section class="offerings">
      <p class="tagline">We do elite level training with youth to professional athletes &amp;<br>brand awareness is our number one concern right now</p>
      <div class="programs">
        <div class="program">
          <div class="program-badge">CLINICS</div>
          <p class="program-note">(1-Day Event to attract<br>50+ Athletes)</p>
        </div>
        <div class="program">
          <div class="program-badge">CAMPS</div>
          <p class="program-note">(2-4 Day Events looking<br>to attract 100+)</p>
        </div>
        <div class="program">
          <div class="program-badge">ACADEMIES</div>
          <p class="program-note">(More intimate and skill<br>specific. lasts 6-8 weeks.<br>10-20 athletes)</p>
        </div>
      </div>
    </section>

    <section class="event-band">
      <h1 class="event-title">K7Z BASEBALL CLINIC</h1>
      <p class="event-date">Date: November 11th, 2017</p>
    </section>

    <section class="details">
      <div class="details-col">
        <div class="details-block">AGES:<br>PREP: (5th to 8th Grade).<br>ELITE (9th-12th Grade)</div>
        <div class="details-block">Registration:<br>8:00am - 9:00 am / 11:00 am - Noon</div>
      </div>
      <div class="details-col">
        <div class="details-block">Times:<br>PREP: 9:00am - 11:00 am<br>ELITE: Noon - 2pm</div>
        <div class="details-block">Investment: $199<br>Current Members: $99</div>
      </div>
    </section>
  </article>
</div>
</body>
</html>
```